Vantrel Telecom Corporate Website & Social Branding

We are looking for a new website for our startup telecom which provides UCaaS, SD-WAN, Business SMS/MMS, Video Conferencing, Managed Network Service & more.

Target Market(s)

Small offices from 1-250 users

Industry/Entity Type

Telecomunications

Coding

Coded - Design and coding required

Colors
0054AA
0677BA
7BADD7
CADEEF
E8F1F8

```html
<!DOCTYPE html>
<html lang="en">
<head>
<meta charset="utf-8">
<title>Vantrel Telecom</title>
<link href="https://fonts.googleapis.com/css2?family=Oswald:wght@300;400;500;600;700&family=Open+Sans:wght@400;600&display=swap" rel="stylesheet">
<style>
:root{
  --blue-deep:#0054AA;
  --blue:#0677BA;
  --blue-soft:#7BADD7;
  --blue-pale:#CADEEF;
  --blue-mist:#E8F1F8;
  --ink:#1d1d1d;
  --text:#333333;
  --band:#efefef;
  --white:#ffffff;
}
*{margin:0;padding:0;box-sizing:border-box}
html,body{width:1200px;height:4566px;overflow:hidden}
body{position:relative;background:var(--white);font-family:"Open Sans",Arial,sans-serif;color:var(--text)}
.page{position:relative;width:1200px;height:4566px;overflow:hidden}
.abs{position:absolute}
.shapes{position:absolute;left:0;top:0}
.heading{font-family:"Oswald",Arial,sans-serif;font-weight:600;color:var(--ink);text-transform:uppercase;letter-spacing:.5px}
.section-title{position:absolute;left:0;width:1200px;text-align:center;font-size:54px;line-height:1}

/* header */
.brand{font-family:"Oswald",Arial,sans-serif;font-weight:600;color:var(--white);display:flex;align-items:center;gap:12px}
.brand .dot{width:34px;height:34px;border-radius:50%;background:var(--blue)}
.site-header .brand{position:absolute;left:186px;top:30px;font-size:34px}
.nav{position:absolute;left:500px;top:38px;display:flex;gap:20px;list-style:none}
.nav li{font-family:"Oswald",Arial,sans-serif;font-size:15px;color:var(--white);letter-spacing:.3px}
.hero-title{position:absolute;left:0;top:220px;width:1200px;text-align:center;color:var(--white);font-size:52px;line-height:56px;font-weight:600}
.btn{position:absolute;display:flex;align-items:center;justify-content:center;background:var(--blue);color:var(--white);font-family:"Oswald",Arial,sans-serif;font-weight:500;font-size:21px;border-radius:40px;text-transform:uppercase}
.btn-hero{left:494px;top:363px;width:212px;height:64px;box-shadow:0 0 0 2px rgba(255,255,255,.15)}

/* about */
.about-title{left:172px;top:762px;font-size:56px}
.about-copy{left:172px;top:838px;width:400px;font-size:15px;line-height:22.5px}
.btn-about{left:172px;top:1019px;width:163px;height:53px;font-size:19px}

/* services */
.service-card{position:absolute;width:264px;height:332px;background:var(--white);border-radius:0 44px 0 44px;box-shadow:0 3px 10px rgba(0,0,0,.12);overflow:hidden;text-align:center}
.service-card .media{height:193px}
.service-card h3{font-family:"Oswald",Arial,sans-serif;font-weight:500;color:var(--blue);font-size:23px;margin-top:14px}
.service-card p{font-size:13px;line-height:18px;margin:8px 26px 0}

/* why */
.why-point{position:absolute;width:180px;font-size:13px;line-height:18px}
.why-point h4{font-family:"Oswald",Arial,sans-serif;font-weight:600;color:var(--ink);font-size:17px;margin-bottom:4px}
.why-point.left{text-align:right}
.why-brand{position:absolute;left:430px;top:2612px;width:340px;justify-content:center;font-size:46px;color:var(--blue-deep)}
.why-brand .dot{width:48px;height:48px;background:var(--blue-soft)}

/* news */
.news-card{position:absolute;width:260px;height:370px;background:var(--white);box-shadow:0 8px 18px rgba(6,119,186,.18)}
.news-card .media{height:186px}
.news-card h3{font-family:"Oswald",Arial,sans-serif;font-weight:500;font-size:18px;line-height:26px;color:var(--ink);margin:18px 18px 0}
.news-card p{font-size:13px;line-height:18px;margin:10px 18px 0}
.news-card .more{display:flex;align-items:center;gap:10px;margin:14px 18px 0;font-family:"Oswald",Arial,sans-serif;font-weight:500;color:var(--blue);font-size:17px}

/* testimonials */
.testimonial{position:absolute;top:3713px;width:260px;text-align:center}
.avatar{width:114px;height:114px;border-radius:50%;margin:0 auto}
.avatar.ring{box-shadow:0 0 0 3px var(--white),0 0 0 5px var(--blue)}
.testimonial blockquote{font-family:"Oswald",Arial,sans-serif;font-weight:300;font-style:italic;font-size:16px;line-height:21px;color:var(--ink);margin-top:38px}
.testimonial cite{display:block;font-style:normal;font-family:"Oswald",Arial,sans-serif;color:var(--blue);font-size:23px;margin-top:24px}

/* footer */
.site-footer{color:var(--white)}
.site-footer .brand{position:absolute;left:172px;top:4265px;font-size:34px}
.socials{position:absolute;left:181px;top:4362px;display:flex;gap:17px}
.socials span{width:42px;height:42px;border-radius:50%;background:#111;display:block}
.foot-col{position:absolute;top:4244px;list-style:none}
.foot-col h4{font-family:"Oswald",Arial,sans-serif;font-weight:600;font-size:20px;margin-bottom:14px;letter-spacing:.4px}
.foot-col li{font-size:14px;line-height:30px}
.foot-col.contact li{display:flex;align-items:center;gap:14px;font-size:15px}
.copyright{position:absolute;left:0;top:4520px;width:1200px;text-align:center;font-size:14px}
.foot-rule{position:absolute;left:172px;top:4502px;width:856px;height:1px;background:rgba(255,255,255,.35)}
</style>
</head>
<body>
<div class="page">

<svg class="shapes" width="1200" height="4566" viewBox="0 0 1200 4566" aria-hidden="true">
  <defs>
    <linearGradient id="heroSky" x1="0" y1="0" x2="0" y2="1">
      <stop offset="0" stop-color="#17233d"/>
      <stop offset=".12" stop-color="#4a4f66"/>
      <stop offset=".2" stop-color="#7a6a6a"/>
      <stop offset=".32" stop-color="#1c2c4c"/>
      <stop offset=".7" stop-color="#0c2a52"/>
      <stop offset="1" stop-color="#123f73"/>
    </linearGradient>
    <linearGradient id="towerScene" x1="0" y1="0" x2="0" y2="1">
      <stop offset="0" stop-color="#cfe3f3"/>
      <stop offset=".45" stop-color="#8fb6d6"/>
      <stop offset="1" stop-color="#2d4a6c"/>
    </linearGradient>
    <linearGradient id="footerBlue" x1="0" y1="0" x2="0" y2="1">
      <stop offset="0" stop-color="#0a86cc"/>
      <stop offset="1" stop-color="#0677BA"/>
    </linearGradient>
  </defs>
  <!-- services band -->
  <polygon points="0,1245 1200,1090 1200,2252 0,2084" fill="var(--band)"/>
  <!-- tower scene area -->
  <polygon role="img" aria-label="Telecom tower with dishes over a city skyline" points="585,760 1200,520 1200,1085 585,1200" fill="url(#towerScene)"/>
  <!-- hero -->
  <path role="img" aria-label="Night city skyline with glowing network lines" d="M0 0H1200V530C900 600 500 650 200 676C90 686 20 650 0 585Z" fill="url(#heroSky)"/>
  <path d="M0 585C20 650 90 686 200 676C500 650 900 600 1200 530" fill="none" stroke="#000" stroke-width="7"/>
  <!-- news band -->
  <polygon points="0,2818 1200,2835 1200,3439 0,3527" fill="var(--band)"/>
  <!-- why choose us arc -->
  <path d="M337 2756A263 263 0 0 1 863 2756" fill="none" stroke="#222" stroke-width="2"/>
  <!-- footer -->
  <path d="M0 4225C300 4160 700 4030 1000 4060C1120 4072 1180 4110 1200 4135V4566H0Z" fill="url(#footerBlue)"/>
  <path d="M0 4225C300 4160 700 4030 1000 4060C1120 4072 1180 4110 1200 4135" fill="none" stroke="#000" stroke-width="6"/>
</svg>

<header class="site-header">
  <div class="brand"><span class="dot"></span>Vantrel Telecom</div>
  <ul class="nav">
    <li>HOME</li><li>PRODUCTS</li><li>SOLUTIONS</li><li>PLAN &amp; PRICING</li><li>RESOURCES</li><li>CONTACT US</li>
  </ul>
  <h1 class="heading hero-title" style="color:var(--white)">Bring Everyone &amp; Everything<br>Together on Vantrel Telecom</h1>
  <div class="btn btn-hero">Get Started</div>
</header>

<section class="about">
  <h2 class="heading abs about-title">About Us</h2>
  <p class="abs about-copy">Lorem ipsum dolor sit amet, consectetur adipiscing elit, sed do eiusmod tempor incididunt ut labore et dolore magna aliqua. Ut enim ad minim veniam, quis nostrud exercitation ullamco te velit esse cillum dolore eu fugiat nulla pariatur.Lorem ipsum dolor sit amet, consectetur adipiscing elit, sed do eiusmod tempor incididunt ut fugiat nulla pariatur.</p>
  <div class="btn btn-about">Read More</div>
</section>

<section class="services">
  <h2 class="heading section-title" style="top:1236px">Our Services</h2>
  <article class="service-card" style="left:172px;top:1345px">
    <div class="media" role="img" aria-label="Glowing cloud communications platform illustration" style="background:linear-gradient(135deg,#1b1e6e,#3a4fd0 55%,#101447)"></div>
    <h3>UCaaS,</h3>
    <p>Lorem ipsum dolor sit amet, consectetur adipiscing elito e e dolore magna aliqua.</p>
  </article>
  <article class="service-card" style="left:464px;top:1345px">
    <div class="media" role="img" aria-label="Digital globe with connected network points" style="background:radial-gradient(circle at 50% 60%,#2ab4d8,#0b5a84 55%,#052a48)"></div>
    <h3>SD-WAN</h3>
    <p>Lorem ipsum dolor sit amet, consectetur adipiscing elito e e dolore magna aliqua.</p>
  </article>
  <article class="service-card" style="left:760px;top:1345px">
    <div class="media" role="img" aria-label="Hands typing on a laptop with message icons" style="background:linear-gradient(135deg,#dfe8f1,#8fb0cf 55%,#4a5e74)"></div>
    <h3>Business SMS/MMS</h3>
    <p>Lorem ipsum dolor sit amet, consectetur adipiscing elito e e dolore magna aliqua.</p>
  </article>
  <article class="service-card" style="left:172px;top:1728px">
    <div class="media" role="img" aria-label="Team in a meeting room joining a video call" style="background:linear-gradient(135deg,#9a8a78,#c9b9a4 50%,#5a4a3c)"></div>
    <h3>Video Conferencing</h3>
    <p>Lorem ipsum dolor sit amet, consectetur adipiscing elito e e dolore magna aliqua.</p>
  </article>
  <article class="service-card" style="left:464px;top:1728px">
    <div class="media" role="img" aria-label="Secure network lock over a keyboard" style="background:linear-gradient(135deg,#1a3870,#5d8ccc 50%,#142a55)"></div>
    <h3>Managed Network</h3>
    <p>Lorem ipsum dolor sit amet, consectetur adipiscing elito e e dolore magna aliqua.</p>
  </article>
  <article class="service-card" style="left:760px;top:1728px">
    <div class="media" role="img" aria-label="Hands on a laptop keyboard with digital icons" style="background:linear-gradient(135deg,#4d4d50,#8a8a8e 50%,#2a2a2c)"></div>
    <h3>Other Services</h3>
    <p>Lorem ipsum dolor sit amet, consectetur adipiscing elito e e dolore magna aliqua.</p>
  </article>
</section>

<section class="why">
  <h2 class="heading section-title" style="top:2303px">Why Choose Us</h2>
  <div class="why-point left" style="left:247px;top:2418px"><h4>Lorem Ipsum</h4>Lorem ipsum dolor sit amet, consectetur dolore magna aliqua.</div>
  <div class="why-point" style="left:800px;top:2418px"><h4>Lorem Ipsum</h4>Lorem ipsum dolor sit amet, consectetur dolore magna aliqua.</div>
  <div class="why-point left" style="left:132px;top:2553px"><h4>Lorem Ipsum</h4>Lorem ipsum dolor sit amet, consectetur dolore magna aliqua.</div>
  <div class="why-point" style="left:895px;top:2553px"><h4>Lorem Ipsum</h4>Lorem ipsum dolor sit amet, consectetur dolore magna aliqua.</div>
  <svg class="shapes" width="1200" height="4566" viewBox="0 0 1200 4566" aria-hidden="true">
    <g fill="var(--blue)" stroke="var(--white)" stroke-width="3">
      <circle cx="489" cy="2485" r="37"/><circle cx="737" cy="2485" r="37"/>
      <circle cx="360" cy="2611" r="37"/><circle cx="842" cy="2611" r="37"/>
    </g>
    <g fill="none" stroke="var(--white)" stroke-width="2.5" stroke-linecap="round" stroke-linejoin="round">
      <circle cx="489" cy="2485" r="14"/><path d="M489 2465v-6M489 2505v6M469 2485h-6M509 2485h6M475 2471l-4-4M503 2499l4 4M503 2471l4-4M475 2499l-4 4"/>
      <circle cx="727" cy="2475" r="5"/><circle cx="749" cy="2478" r="5"/><circle cx="733" cy="2498" r="5"/><path d="M731 2478l13 0M729 2480l3 13M745 2482l-9 12"/>
      <path d="M360 2590l17 6v12c0 11-8 18-17 22c-9-4-17-11-17-22v-12z"/><path d="M352 2610l6 6l11-12"/>
      <circle cx="842" cy="2611" r="18"/><ellipse cx="842" cy="2611" rx="8" ry="18"/><path d="M824 2611h36M827 2601h30M827 2621h30"/>
    </g>
  </svg>
  <div class="brand why-brand"><span class="dot"></span>Vantrel Telecom</div>
</section>

<section class="news">
  <h2 class="heading section-title" style="top:2917px">Latest News</h2>
  <article class="news-card" style="left:172px;top:3013px">
    <div class="media" role="img" aria-label="Business team on a video conference screen" style="background:linear-gradient(135deg,#3b4c63,#9fb0c2 55%,#e8e6e2)"></div>
    <h3>Lorem ipsum dolor sit amet, consectetur</h3>
    <p>Lorem ipsum dolor sit amet, consectetur adipiscing elit, sed aliqua.</p>
    <div class="more">GET STORY <svg width="22" height="16" viewBox="0 0 22 16"><path d="M1 8h18M12 1l7 7l-7 7" fill="none" stroke="var(--blue)" stroke-width="2.5"/></svg></div>
  </article>
  <article class="news-card" style="left:468px;top:3013px">
    <div class="media" role="img" aria-label="Hand holding a phone with a messaging app" style="background:linear-gradient(135deg,#f1f1f1,#d9d3d6 55%,#e7b9c6)"></div>
    <h3>Lorem ipsum dolor sit amet, consectetur</h3>
    <p>Lorem ipsum dolor sit amet, consectetur adipiscing elit, sed aliqua.</p>
    <div class="more">GET STORY <svg width="22" height="16" viewBox="0 0 22 16"><path d="M1 8h18M12 1l7 7l-7 7" fill="none" stroke="var(--blue)" stroke-width="2.5"/></svg></div>
  </article>
  <article class="news-card" style="left:767px;top:3013px">
    <div class="media" role="img" aria-label="Laptop keyboard with connected people icons" style="background:linear-gradient(135deg,#dbe9f5,#7fb4dc 55%,#3a78a8)"></div>
    <h3>Lorem ipsum dolor sit amet, consectetur</h3>
    <p>Lorem ipsum dolor sit amet, consectetur adipiscing elit, sed aliqua.</p>
    <div class="more">GET STORY <svg width="22" height="16" viewBox="0 0 22 16"><path d="M1 8h18M12 1l7 7l-7 7" fill="none" stroke="var(--blue)" stroke-width="2.5"/></svg></div>
  </article>
</section>

<section class="testimonials">
  <h2 class="heading section-title" style="top:3585px">Testimonial</h2>
  <figure class="testimonial" style="left:170px">
    <div class="avatar" role="img" aria-label="Portrait of a customer" style="background:radial-gradient(circle,#b9b9b9,#7d7d7d)"></div>
    <blockquote>"Lorem ipsum dolor sit amet, consectetur sed do &nbsp;incididunt ut labore et laborum."</blockquote>
    <cite>MARLOW</cite>
  </figure>
  <figure class="testimonial" style="left:470px">
    <div class="avatar ring" role="img" aria-label="Portrait of a customer" style="background:radial-gradient(circle,#f4f4f4,#dcdcdc)"></div>
    <blockquote>"Lorem ipsum dolor sit amet, consectetur sed do &nbsp;incididunt ut labore et laborum."</blockquote>
    <cite>DEAN ASHBY</cite>
  </figure>
  <figure class="testimonial" style="left:770px">
    <div class="avatar" role="img" aria-label="Portrait of a customer" style="background:radial-gradient(circle,#f2f2f2,#d6d6d6)"></div>
    <blockquote>"Lorem ipsum dolor sit amet, consectetur sed do &nbsp;incididunt ut labore et laborum."</blockquote>
    <cite>LIORA</cite>
  </figure>
</section>

<footer class="site-footer">
  <div class="brand"><span class="dot" style="background:var(--blue-pale)"></span>Vantrel Telecom</div>
  <div class="socials"><span></span><span></span><span></span></div>
  <ul class="foot-col" style="left:427px">
    <h4>PRODUCTS</h4>
    <li>UCaaS</li><li>SD-WAN</li><li>Business SMS/MMS</li><li>Video Conferencing,</li><li>Managed Network Service</li>
  </ul>
  <ul class="foot-col contact" style="left:645px">
    <h4>CONTACT US</h4>
    <li><svg width="18" height="18" viewBox="0 0 24 24"><path d="M6.6 10.8a15 15 0 0 0 6.6 6.6l2.2-2.2c.3-.3.7-.4 1-.2c1.1.4 2.3.6 3.6.6c.6 0 1 .4 1 1V20c0 .6-.4 1-1 1A17 17 0 0 1 3 4c0-.6.4-1 1-1h3.5c.6 0 1 .4 1 1c0 1.3.2 2.5.6 3.6c.1.3 0 .7-.2 1z" fill="var(--white)"/></svg>(800) 555-0142 Tollfree</li>
    <li><svg width="18" height="18" viewBox="0 0 24 24"><path d="M6.6 10.8a15 15 0 0 0 6.6 6.6l2.2-2.2c.3-.3.7-.4 1-.2c1.1.4 2.3.6 3.6.6c.6 0 1 .4 1 1V20c0 .6-.4 1-1 1A17 17 0 0 1 3 4c0-.6.4-1 1-1h3.5c.6 0 1 .4 1 1c0 1.3.2 2.5.6 3.6c.1.3 0 .7-.2 1z" fill="var(--white)"/></svg>(415) 555-0187 Office</li>
    <li><svg width="18" height="18" viewBox="0 0 24 24"><path d="M6.6 10.8a15 15 0 0 0 6.6 6.6l2.2-2.2c.3-.3.7-.4 1-.2c1.1.4 2.3.6 3.6.6c.6 0 1 .4 1 1V20c0 .6-.4 1-1 1A17 17 0 0 1 3 4c0-.6.4-1 1-1h3.5c.6 0 1 .4 1 1c0 1.3.2 2.5.6 3.6c.1.3 0 .7-.2 1z" fill="var(--white)"/></svg>(415) 555-0193 Direct /SMS</li>
    <li><svg width="18" height="14" viewBox="0 0 24 18"><rect x="1" y="1" width="22" height="16" rx="2" fill="var(--white)"/><path d="M2 2l10 8l10-8" fill="none" stroke="var(--blue)" stroke-width="2"/></svg>hello@vantreltelecom.com</li>
  </ul>
  <ul class="foot-col" style="left:922px">
    <h4>QUICK LINKS</h4>
    <li>Home</li><li>Products</li><li>Solutions</li><li>Plans &amp; Pricing</li><li>Resources</li><li>contact us</li>
  </ul>
  <div class="foot-rule"></div>
  <p class="copyright">Copyrights © 2022 &nbsp;Vantrel Telecom I All Rights Reversed</p>
</footer>

</div>
</body>
</html>
```